New Shopify design for existing webshop

We have an existing webshop on an old Magento solution. Now we're going to switch to Shopify. We need a new Shopify theme for this.

Our old website is www.tessin-brand.ch

We have the product categories:
Postage stamps
Tobler albums & accessories
Coins and banknotes
Franking service

In addition, we need the pages to be prominently integrated similar to the products:
Missing list service
Purchases

We can include the following pages at the bottom, less prominently on the page:
Contact
imprint
Conditions
revocation
data protection

shipping
Guarantee of trust

The products should be in the foreground on the website. Our logo can be incorporated. We also upload some images that can be used for the design. Of course you don't have to.

The new design does not have to be based on the old design. It can be something completely new. All pictures that we have on the website can of course also be used. But I also added some pictures to the project that fit our company.

Our company:
The company, which was founded by Paul Tobler in 1922, has developed into one of the largest and best-known Swiss postage stamp houses over the past 98 years.

Target Market(s)

Germany, Switzerland

Font styles to use
Serif
Sans Serif

Requirements
Must have
• The products stamps that you can buy should be in the foreground.
If images are used in the design, please focus on Swiss stamps and coins (no foreign coins or stamps)

```html
<!DOCTYPE html>
<html lang="de">
<head>
<meta charset="utf-8">
<title>Tessin Brand – Briefmarken, Münzen & Zubehör</title>
<link href="https://fonts.googleapis.com/css2?family=Playfair+Display:wght@700;900&family=Roboto:wght@400;500;700&family=Courier+Prime&display=swap" rel="stylesheet">
<style>
:root{
  --navy:#0f1a2b;
  --red:#d3202f;
  --ink:#222;
  --muted:#555;
  --header:#ebebeb;
  --nav:#f6f6f6;
  --map-band:#5e5e5e;
  --footer:#e9e9e9;
  --line:#cfcfcf;
}
*{box-sizing:border-box;margin:0;padding:0}
html,body{width:1200px;height:3623px;overflow:hidden}
body{position:relative;background:#fff;font-family:'Roboto',sans-serif;color:var(--ink)}
.abs{position:absolute}
.mono{font-family:'Courier Prime',monospace}
.serif{font-family:'Playfair Display',serif}

/* top bar */
.topbar{left:0;top:0;width:1200px;height:44px;background:var(--navy);color:#fff;font-size:14px}
.topbar span{position:absolute;top:13px;display:flex;align-items:center;gap:7px}
/* header */
.header{left:0;top:44px;width:1200px;height:74px;background:var(--header)}
.brand{display:flex;align-items:center;gap:8px;font-family:'Roboto',sans-serif;font-weight:700;font-size:19px;color:var(--red);letter-spacing:.5px}
.brand i{display:block;width:14px;height:14px;background:var(--red)}
.cat{left:357px;top:22px;width:149px;height:30px;background:#ddd;font-size:13px;font-weight:700;padding:8px 12px}
.search{left:506px;top:22px;width:268px;height:30px;background:#fff;font-size:12px;color:#999;font-style:italic;padding:8px 14px}
.search-btn{left:774px;top:22px;width:39px;height:30px;background:#222;display:flex;align-items:center;justify-content:center}
.account{left:841px;top:22px;font-size:12px;line-height:14px;color:#444}
.divider{left:961px;top:18px;width:1px;height:38px;background:#aaa}
.cart{left:993px;top:29px;font-size:12px;color:#444}
/* nav */
.nav{left:0;top:118px;width:1200px;height:59px;background:var(--nav);font-size:13px;color:#333}
.nav span{position:absolute;top:21px}
/* hero */
.hero{left:0;top:177px;width:1200px;height:650px;
  background:radial-gradient(ellipse 330px 260px at 560px 330px,#8a5a3c 0%,#5d4132 45%,transparent 75%),
  radial-gradient(ellipse 230px 150px at 760px 120px,#9b6b4c 0%,transparent 80%),
  linear-gradient(135deg,#404448 0%,#2c3034 50%,#3b3e40 100%)}
.hero h1{left:210px;top:200px;font-size:50px;font-weight:700;color:#fff;white-space:nowrap}
.hero h1 em{font-style:normal;color:var(--red)}
.hero p{left:210px;top:285px;font-size:18px;font-weight:700;color:#fff}
.shop{left:212px;top:397px;width:169px;height:38px;background:var(--red);color:#fff;font-size:13px;font-weight:700;display:flex;align-items:center;justify-content:center}
.dots{left:570px;top:571px;display:flex;gap:8px}
.dots b{width:8px;height:8px;border-radius:50%;background:#fff}
.dots b:first-child{background:var(--red)}
/* section titles */
.title{font-family:'Playfair Display',serif;font-weight:900;font-size:48px;color:#222;left:146px;white-space:nowrap}
/* product cards */
.card{width:212px;height:326px;background:#fff;box-shadow:0 1px 6px rgba(0,0,0,.15)}
.card .img{position:absolute;left:0;top:0;width:212px;height:142px;border-bottom:2px solid var(--red)}
.card .name{position:absolute;top:163px;width:100%;text-align:center;font-size:13px;color:#333}
.card .price{position:absolute;top:192px;width:100%;text-align:center;font-size:13px;color:var(--red)}
.card .buy{position:absolute;left:18px;top:230px;width:176px;height:31px;background:var(--red);color:#fff;font-size:13px;display:flex;align-items:center;justify-content:center}
.card .wish{position:absolute;left:18px;top:272px;width:176px;height:32px;border:1px solid #555;font-size:13px;display:flex;align-items:center;justify-content:center}
.arrow{width:36px;height:40px;background:#fff;box-shadow:0 1px 4px rgba(0,0,0,.2);display:flex;align-items:center;justify-content:center}
/* news */
.news{left:0;top:2204px;width:1196px;height:244px;background:radial-gradient(circle at 1050px 120px,#6b4a1e 0,#2a2012 30%,transparent 60%),linear-gradient(90deg,#2b2b2b,#1d1d1d)}
.news h2{left:176px;top:80px;font-size:46px;color:#fff;font-weight:700}
.news .uline{left:216px;top:140px;width:60px;height:3px;background:var(--red)}
.news-box{left:512px;top:19px;width:533px;height:204px;background:var(--red);color:#fff;padding:22px 16px}
.news-box h3{font-size:17px;font-weight:700;line-height:21px}
.news-box p{margin-top:14px;font-size:12.5px;line-height:21px}
/* location */
.locate{left:0;top:2508px;width:1200px;height:327px;background:var(--map-band)}
.map{left:159px;top:41px;width:536px;height:251px;background:linear-gradient(135deg,#e6e8ea,#d4dadd 60%,#cfd6c8)}
.loc-text{left:719px;font-family:'Playfair Display',serif;color:#fff}
.loc-head{top:67px;font-size:11px;font-weight:700}
.loc-item{display:flex;gap:10px;font-size:14px;font-weight:700;line-height:16px}
.contact-big{left:719px;top:222px;font-family:'Playfair Display',serif;font-weight:700;font-size:48px;color:rgba(255,255,255,.28);white-space:nowrap}
/* get in touch */
.touch-title{left:148px;top:2890px;font-family:'Playfair Display',serif;font-weight:700;font-size:48px}
.touch-sub{left:238px;top:2941px;font-size:13px;color:#333}
.tcard{width:279px;height:226px;background:#fff;box-shadow:0 1px 6px rgba(0,0,0,.15)}
.tcard .img{position:absolute;left:0;top:0;width:100%;height:163px;border-bottom:3px solid var(--red)}
.tcard .lbl{position:absolute;top:186px;width:100%;text-align:center;font-size:17px;font-weight:700}
/* footer */
.footer{left:0;top:3278px;width:1200px;height:345px;background:var(--footer)}
.fcol{font-size:13px;color:#333;line-height:34px}
.newsletter h4{font-family:'Playfair Display',serif;font-size:18px;font-weight:700}
.newsletter p{font-size:11.5px;color:#555;margin-top:18px}
.nl-input{margin-top:30px;width:249px;height:34px;border:1px solid #aaa;background:#f4f4f4;font-size:11.5px;color:#555;padding:10px 14px}
.nl-btn{margin-top:18px;width:249px;height:34px;background:var(--red);color:#fff;font-size:12px;font-weight:700;display:flex;align-items:center;justify-content:center}
.social{margin-top:24px;display:flex;gap:36px;padding-left:3px}
.social i{display:block;width:11px;height:11px;border-radius:50%;background:#555}
.legal{left:0;top:318px;width:1170px;text-align:center;font-size:11px;color:#333}
</style>
</head>
<body>

<div class="abs topbar mono">
  <span style="left:150px"><svg width="14" height="14"><circle cx="7" cy="7" r="6" fill="#d3202f"/><rect x="4" y="5" width="6" height="4" fill="#fff"/></svg>info@tessin-brand.ch</span>
  <span style="left:500px"><svg width="12" height="15"><path d="M6 0a6 6 0 0 1 6 6c0 4-6 9-6 9S0 10 0 6a6 6 0 0 1 6-6z" fill="#d3202f"/><circle cx="6" cy="6" r="2" fill="#0f1a2b"/></svg>Werkstrasse 7, 4410 Liestal</span>
  <span style="left:918px"><svg width="15" height="15"><path d="M3 1l3 3-2 2c1 2 3 4 5 5l2-2 3 3-2 2C7 14 1 8 1 3z" fill="#d3202f"/></svg>0041615550182</span>
</div>

<div class="abs header">
  <div class="abs brand" style="left:136px;top:27px"><i></i>TESSIN BRAND</div>
  <div class="abs cat">All Categories ▾</div>
  <div class="abs search">Search...</div>
  <div class="abs search-btn"><svg width="16" height="16"><circle cx="9" cy="7" r="5" fill="none" stroke="#fff" stroke-width="1.6"/><line x1="5.5" y1="10.5" x2="1.5" y2="14.5" stroke="#fff" stroke-width="1.6"/></svg></div>
  <div class="abs account mono">Login/ Signup<br><b>My account ▾</b></div>
  <div class="abs divider"></div>
  <div class="abs cart">My Cart</div>
</div>

<nav class="abs nav mono">
  <span style="left:145px">postage stamps</span>
  <span style="left:276px">Tobler albums &amp; accessories</span>
  <span style="left:504px">Coins &amp; Banknotes</span>
  <span style="left:657px">Missing List Servince</span>
  <span style="left:842px">Franking service</span>
  <span style="left:989px">Purchases</span>
</nav>

<section class="abs hero" role="img" aria-label="Close-up photograph of a copper coin on a dark surface">
  <h1 class="abs serif">Sir Suchen und Kaufen <em>GOLD</em> &amp; <em>SILBER</em></h1>
  <p class="abs">wir sind beinnahe 100 Jae im Handel mit Briefmarken</p>
  <div class="abs shop">SHOP NOW</div>
  <svg class="abs" style="left:62px;top:288px" width="20" height="40"><polyline points="18,2 2,20 18,38" fill="none" stroke="#ddd" stroke-width="2"/></svg>
  <svg class="abs" style="left:1118px;top:295px" width="20" height="40"><polyline points="2,2 18,20 2,38" fill="none" stroke="#ddd" stroke-width="2"/></svg>
  <div class="abs dots"><b></b><b></b><b></b><b></b></div>
</section>

<!-- Briefmarken -->
<h2 class="abs title" style="top:836px">Briefmarken</h2>
<div class="abs arrow" style="left:68px;top:1068px"><svg width="12" height="20"><polyline points="10,1 2,10 10,19" fill="none" stroke="#666" stroke-width="1.5"/></svg></div>
<div class="abs arrow" style="left:1095px;top:1070px"><svg width="12" height="20"><polyline points="2,1 10,10 2,19" fill="none" stroke="#666" stroke-width="1.5"/></svg></div>

<div class="abs card" style="left:151px;top:926px"><div class="img" role="img" aria-label="Swiss stamp pair 1944 Olympic committee" style="background:linear-gradient(90deg,#fff 6%,#8a2c1e 6%,#b0553a 35%,#2a1a10 42%,#2a1a10 58%,#b0553a 65%,#8a2c1e 94%,#fff 94%);background-size:100% 52%;background-repeat:no-repeat;background-position:center"></div><div class="name">1944, OLYMP. KOMITEE</div><div class="price">Fr. 38,92</div><div class="buy">IN DEN WARENKORB</div><div class="wish">Auf den Wunschzettel</div></div>
<div class="abs card" style="left:379px;top:926px"><div class="img" role="img" aria-label="Swiss 65 Rp Ikarus stamp" style="background:radial-gradient(ellipse 80px 50px at center,#6fb9bc,#3f8f96 70%,#fff 72%)"></div><div class="name">65 RP. IKARUS</div><div class="price">Fr. 14,80</div><div class="buy">IN DEN WARENKORB</div><div class="wish">Auf den Wunschzettel</div></div>
<div class="abs card" style="left:609px;top:926px"><div class="img" role="img" aria-label="1941 Anbauwerk stamp in brown tones" style="background:radial-gradient(ellipse 100px 62px at center,#8a6a52,#5a3c2c 70%,#fff 72%)"></div><div class="name">1941, ANBAUWERK</div><div class="price">Fr. 4,90</div><div class="buy">IN DEN WARENKORB</div><div class="wish">Auf den Wunschzettel</div></div>
<div class="abs card" style="left:837px;top:926px"><div class="img" role="img" aria-label="Emmental special souvenir sheet stamps" style="background:radial-gradient(ellipse 92px 55px at center,#8fa7d8,#4b5f9a 70%,#fff 72%)"></div><div class="name">EMMENTAL, SONDERBLOCK</div><div class="price">Fr. 4,90</div><div class="buy">IN DEN WARENKORB</div><div class="wish">Auf den Wunschzettel</div></div>

<!-- Albums -->
<h2 class="abs title" style="top:1282px">Tobler albums &amp; accessories</h2>
<div class="abs arrow" style="left:68px;top:1515px"><svg width="12" height="20"><polyline points="10,1 2,10 10,19" fill="none" stroke="#666" stroke-width="1.5"/></svg></div>
<div class="abs arrow" style="left:1095px;top:1517px"><svg width="12" height="20"><polyline points="2,1 10,10 2,19" fill="none" stroke="#666" stroke-width="1.5"/></svg></div>

<div class="abs card" style="left:151px;top:1372px"><div class="img" role="img" aria-label="Luxury stamp tweezers" style="background:linear-gradient(170deg,#fff 45%,#8a8f93 48%,#fff 52%)"></div><div class="name">PINZETTE 42, LUXUS</div><div class="price">Fr. 38,92</div><div class="buy">IN DEN WARENKORB</div><div class="wish">Auf den Wunschzettel</div></div>
<div class="abs card" style="left:379px;top:1372px"><div class="img" role="img" aria-label="Open navy first-day-cover album" style="background:radial-gradient(ellipse 95px 50px at center,#3a5ba8,#13244f 70%,#fff 74%)"></div><div class="name">FDC-ALBUM,</div><div class="price">Fr. 14,80</div><div class="buy">IN DEN WARENKORB</div><div class="wish">Auf den Wunschzettel</div></div>
<div class="abs card" style="left:609px;top:1372px"><div class="img" role="img" aria-label="Black magnifying loupes" style="background:linear-gradient(135deg,#dfe2e4,#9da2a6 50%,#c9ccce)"></div><div class="name">1941, ANBAUWERK</div><div class="price">Fr. 4,90</div><div class="buy">IN DEN WARENKORB</div><div class="wish">Auf den Wunschzettel</div></div>
<div class="abs card" style="left:837px;top:1372px"><div class="img" role="img" aria-label="UV test lamp" style="background:linear-gradient(160deg,#c9cbcd,#3b3f44 45%,#2a2d32 60%,#b7babd)"></div><div class="name">UV-TESTLAMPE</div><div class="price">Fr. 4,90</div><div class="buy">IN DEN WARENKORB</div><div class="wish">Auf den Wunschzettel</div></div>

<!-- Münzen -->
<h2 class="abs title" style="top:1726px;left:144px">Münzen &amp; Banknoten</h2>
<div class="abs arrow" style="left:68px;top:1961px"><svg width="12" height="20"><polyline points="10,1 2,10 10,19" fill="none" stroke="#666" stroke-width="1.5"/></svg></div>
<div class="abs arrow" style="left:1095px;top:1963px"><svg width="12" height="20"><polyline points="2,1 10,10 2,19" fill="none" stroke="#666" stroke-width="1.5"/></svg></div>

<div class="abs card" style="left:151px;top:1819px"><div class="img" role="img" aria-label="Swiss gold coins, front and back" style="background:radial-gradient(circle at 30% 50%,#e0b455,#b5852a 42px,transparent 44px),radial-gradient(circle at 70% 50%,#e0b455,#b5852a 42px,transparent 44px),#fff"></div><div class="name">PINZETTE 42, LUXUS</div><div class="price">Fr. 38,92</div><div class="buy">IN DEN WARENKORB</div><div class="wish">Auf den Wunschzettel</div></div>
<div class="abs card" style="left:379px;top:1819px"><div class="img" role="img" aria-label="Open navy first-day-cover album" style="background:radial-gradient(ellipse 95px 50px at center,#3a5ba8,#13244f 70%,#fff 74%)"></div><div class="name">FDC-ALBUM,</div><div class="price">Fr. 14,80</div><div class="buy">IN DEN WARENKORB</div><div class="wish">Auf den Wunschzettel</div></div>
<div class="abs card" style="left:609px;top:1819px"><div class="img" role="img" aria-label="Black magnifying loupes" style="background:linear-gradient(135deg,#dfe2e4,#9da2a6 50%,#c9ccce)"></div><div class="name">1941, ANBAUWERK</div><div class="price">Fr. 4,90</div><div class="buy">IN DEN WARENKORB</div><div class="wish">Auf den Wunschzettel</div></div>
<div class="abs card" style="left:837px;top:1819px"><div class="img" role="img" aria-label="UV test lamp" style="background:linear-gradient(160deg,#c9cbcd,#3b3f44 45%,#2a2d32 60%,#b7babd)"></div><div class="name">UV-TESTLAMPE</div><div class="price">Fr. 4,90</div><div class="buy">IN DEN WARENKORB</div><div class="wish">Auf den Wunschzettel</div></div>

<!-- News -->
<section class="abs news" role="img" aria-label="Dark background with warm blurred bokeh lights">
  <h2 class="abs serif">Recent News</h2>
  <div class="abs uline"></div>
  <div class="abs news-box">
    <h3>Lorem ipsum dolor sit amet, consectetur adipisicing elit, sed do eiusmod tempor incididunt ut labore et dolore magna aliqua.</h3>
    <p>Lorem ipsum dolor sit amet, consectetur adipiscing elit, sed do eiusmod tempor incididunt ut labore et dolore magna aliqua. Quis ipsum suspendisse ultrices gravida. Risus commodo viverra maecenas accumsan lacus vel facilisis.</p>
  </div>
</section>

<!-- Location -->
<section class="abs locate">
  <div class="abs map" role="img" aria-label="Site map of the industrial estate showing the shop location"></div>
  <div class="abs loc-text loc-head">Waar kunt u ons vinden</div>
  <div class="abs loc-text loc-item" style="top:90px"><svg width="10" height="14"><path d="M5 0a5 5 0 0 1 5 5c0 3-5 9-5 9S0 8 0 5a5 5 0 0 1 5-5z" fill="#d3202f"/></svg><span>Werkstrasse 7,<br>4410 Liestal, Switzerland</span></div>
  <div class="abs loc-text loc-item" style="top:145px"><svg width="11" height="11"><circle cx="5.5" cy="5.5" r="5" fill="#d3202f"/></svg><span>info@tessin-brand.ch</span></div>
  <div class="abs loc-text loc-item" style="top:188px"><svg width="11" height="11"><path d="M2 0l3 3-2 2c1 1 2 2 3 3l2-2 3 3-2 2C5 11 0 6 0 2z" fill="#d3202f"/></svg><span>0041615550182</span></div>
  <div class="abs contact-big">Neem contact op</div>
</section>

<!-- Get in touch -->
<h2 class="abs touch-title">Get in touch</h2>
<div class="abs touch-sub">We'd love to hear from you</div>
<div class="abs tcard" style="left:151px;top:2992px"><div class="img" role="img" aria-label="Office worker on the phone in a bright office" style="background:linear-gradient(90deg,#9aa09a,#e9e9e6 50%,#cfcfcb)"></div><div class="lbl">7/24 Service</div></div>
<div class="abs tcard" style="left:461px;top:2992px"><div class="img" role="img" aria-label="Laptop on a white desk" style="background:linear-gradient(180deg,#f1f1f0,#d9d9d8 70%,#b9b9b9)"></div><div class="lbl">Technical Support</div></div>
<div class="abs tcard" style="left:771px;top:2992px"><div class="img" role="img" aria-label="Portrait of a man in a suit on a dark background" style="background:radial-gradient(ellipse at 50% 70%,#2c3c66,#121826 70%)"></div><div class="lbl">Find a Distributor</div></div>

<!-- Footer -->
<footer class="abs footer">
  <div class="abs brand" style="left:145px;top:66px"><i></i>TESSIN BRAND</div>
  <div class="abs fcol" style="left:356px;top:49px">ABOUT US<br>SHIPPING<br>GUARANTEE OF TRUST</div>
  <div class="abs fcol" style="left:530px;top:49px">SUPPORT<br>CONTACT<br>IMPRINT<br>CONDITION<br>REVOCATION<br>DATA PROTECTION</div>
  <div class="abs newsletter" style="left:761px;top:54px">
    <h4>Newsletter</h4>
    <p>Get updates and exclusive offers by email</p>
    <div class="nl-input">Enter your email</div>
    <div class="nl-btn">Sign Up</div>
    <div class="social"><i></i><i></i><i></i><i></i></div>
  </div>
  <div class="abs legal">PRIVACY &amp; SECURITY &nbsp;|&nbsp; TERMS &amp; CONDITIONS</div>
</footer>

</body>
</html>
```